The Marlowe Company Truck Wrap

Need a vehicle wrap design for various white colored Velko Pick Up Trucks, sides, tailgate and hood only. Company logo, tagline, phone number, website, contractor license, QTN logo and A+ rating. Looking for brand consistency with colors, fonts and style. I've uploaded some of our current marketing for you to see. Looking for bold, eyecatching but easy to see and read. Not too cluttered up. Creative and Unique.

Target Market(s)

Residential contracting

Industry/Entity Type

Roofing

Font styles to use
Sans Serif

Colors
0054AA
0677BA
7BADD7
CADEEF
E8F1F8
00AB8E
00BBA5
67D7C9
C6EFE9
E9F9F6
59FF00
82FF00
B8FF75
E3FFCB
F4FFEA
FFC000
F8CF3A
FAE287
FDF2CF
FEFAEE
EE7325
F08F49
F5BC92
FAE3D3
FDF4ED

Requirements
Must have
• Company contact information
Nice to have
• Simple but eye catching; consistent branding
Should not have
• Too much graphic

```html
<!DOCTYPE html>
<html lang="en">
<head>
<meta charset="utf-8">
<title>The Marlowe Company Truck Wrap</title>
<link href="https://fonts.googleapis.com/css2?family=Ubuntu:wght@500;700&family=Roboto:ital,wght@1,700&display=swap" rel="stylesheet">
<style>
  :root {
    --bg-top: #3a3a3a;
    --bg-bottom: #141414;
    --orange: #f39314;
    --blue: #0677ba;
    --navy: #0054aa;
    --green: #5cbf12;
    --white: #ffffff;
    --panel-white: #e8f1f8;
  }
  html, body {
    margin: 0;
    width: 1200px;
    height: 1200px;
    overflow: hidden;
  }
  body {
    background: radial-gradient(ellipse at 50% 10%, var(--bg-top), var(--bg-bottom) 75%);
    position: relative;
    font-family: "Ubuntu", sans-serif;
  }
  .wrap-panel { position: absolute; display: block; }
  .side-right { left: 160px; top: 70px; width: 880px; height: 240px; }
  .side-left  { left: 160px; top: 420px; width: 880px; height: 240px; }
  .tailgate   { left: 320px; top: 790px; width: 560px; height: 300px; }
  .fill-orange { fill: var(--orange); }
  .fill-blue { fill: var(--blue); }
  .fill-green { fill: var(--green); }
  .fill-white { fill: var(--panel-white); }
  .pinstripe { fill: none; stroke: var(--white); stroke-width: 4; }
  .logo-mark { fill: var(--orange); }
  .tagline { font-family: "Ubuntu", sans-serif; font-weight: 700; fill: var(--white); }
  .brand-name { font-family: "Ubuntu", sans-serif; font-weight: 500; fill: var(--navy); }
  .brand-sub { font-family: "Ubuntu", sans-serif; font-weight: 500; fill: var(--green); }
  .phone, .web, .license { font-family: "Roboto", sans-serif; font-style: italic; font-weight: 700; fill: var(--white); }
</style>
</head>
<body>

<svg class="wrap-panel side-right" viewBox="0 0 880 240" aria-label="Passenger side wrap">
  <rect class="fill-orange" width="880" height="240" rx="10"/>
  <polygon class="fill-blue" points="230,0 600,0 700,240 290,240"/>
  <polygon class="fill-white" points="280,0 565,0 630,190 300,190"/>
  <polygon class="fill-green" points="600,0 880,0 880,240 705,240"/>
  <line class="pinstripe" x1="598" y1="0" x2="703" y2="240"/>
  <g role="img" aria-label="Company logo mark"><rect class="logo-mark" x="417" y="10" width="40" height="40"/></g>
  <text class="tagline" x="130" y="58" font-size="28" text-anchor="middle">We Treat</text>
  <text class="tagline" x="130" y="92" font-size="28" text-anchor="middle">You Like Family</text>
  <text class="brand-name" x="437" y="86" font-size="34" text-anchor="middle">THE MARLOWE</text>
  <text class="brand-name" x="440" y="118" font-size="28" text-anchor="middle">COMPANY</text>
  <text class="brand-sub" x="445" y="146" font-size="19" text-anchor="middle">ROOFING AND SOLAR</text>
  <text class="license" x="470" y="220" font-size="20" text-anchor="middle">LIC. #CCC1048215</text>
  <text class="phone" x="775" y="90" font-size="28" text-anchor="middle">555-014-7722</text>
  <text class="web" x="775" y="114" font-size="15" text-anchor="middle">MarloweRoofs.com</text>
</svg>

<svg class="wrap-panel side-left" viewBox="0 0 880 240" aria-label="Driver side wrap">
  <rect class="fill-orange" width="880" height="240" rx="10"/>
  <g transform="translate(880 0) scale(-1 1)">
    <polygon class="fill-blue" points="230,0 600,0 700,240 290,240"/>
    <polygon class="fill-white" points="280,0 565,0 630,190 300,190"/>
    <polygon class="fill-green" points="600,0 880,0 880,240 705,240"/>
    <line class="pinstripe" x1="598" y1="0" x2="703" y2="240"/>
  </g>
  <g role="img" aria-label="Company logo mark"><rect class="logo-mark" x="423" y="10" width="40" height="40"/></g>
  <text class="tagline" x="750" y="58" font-size="28" text-anchor="middle">We Treat</text>
  <text class="tagline" x="750" y="92" font-size="28" text-anchor="middle">You Like Family</text>
  <text class="brand-name" x="443" y="86" font-size="34" text-anchor="middle">THE MARLOWE</text>
  <text class="brand-name" x="440" y="118" font-size="28" text-anchor="middle">COMPANY</text>
  <text class="brand-sub" x="435" y="146" font-size="19" text-anchor="middle">ROOFING AND SOLAR</text>
  <text class="license" x="410" y="220" font-size="20" text-anchor="middle">LIC. #CCC1048215</text>
  <text class="phone" x="105" y="90" font-size="28" text-anchor="middle">555-014-7722</text>
  <text class="web" x="105" y="114" font-size="15" text-anchor="middle">MarloweRoofs.com</text>
</svg>

<svg class="wrap-panel tailgate" viewBox="0 0 560 300" aria-label="Tailgate wrap">
  <rect class="fill-orange" width="560" height="300" rx="10"/>
  <polygon class="fill-blue" points="20,0 420,0 370,300 80,300"/>
  <polygon class="fill-white" points="70,0 380,0 330,215 110,215"/>
  <line class="pinstripe" x1="425" y1="0" x2="375" y2="300"/>
  <g role="img" aria-label="Company logo mark"><rect class="logo-mark" x="205" y="12" width="40" height="40"/></g>
  <text class="brand-name" x="225" y="92" font-size="32" text-anchor="middle">THE MARLOWE</text>
  <text class="brand-name" x="225" y="124" font-size="27" text-anchor="middle">COMPANY</text>
  <text class="brand-sub" x="225" y="152" font-size="18" text-anchor="middle">ROOFING AND SOLAR</text>
  <text class="phone" x="225" y="252" font-size="28" text-anchor="middle">555-014-7722</text>
  <text class="web" x="225" y="278" font-size="16" text-anchor="middle">MarloweRoofs.com</text>
  <text class="tagline" x="482" y="110" font-size="32" text-anchor="middle">We Treat</text>
  <text class="tagline" x="482" y="150" font-size="32" text-anchor="middle">You Like</text>
  <text class="tagline" x="482" y="190" font-size="32" text-anchor="middle">Family</text>
</svg>

</body>
</html>
```